Professional banners for an eyewear company

I have 3 images which need to be made into banners. Size 990 x 370, with a 10 pixel white border at top and bottom of banner.

They all need to be adjusted to make the colours better and less bright.
All will need some writing written on them with a nice serif font.

Banner 1 text: Handcrafted luxury eyewear, with a purpose...
Banner 2 text: Half of our profits go to help malnourished children in India
Banner 3 text: 10% of your first order, use code: First Order

On our homepage these 3 banners will alternate, so they need to look good together.

Tips
Please take a look at the banners on the lunvoreck.com homepage, this is kind of how I want the text to be displayed, and they use good colours.

The backgrounds on Banners 2 & 3 can be changed.
Banner 3 background if you can change to a nice colour, as per lunvoreck.com homepage.
Updates

Hi, just a quick update, thank you for all the designs submitted so far, please keep in mind that the brand is a luxury high-end brand so designs will need to reflect this.

Industry/Entity Type

Eyewear

```html
<!DOCTYPE html>
<html lang="en">
<head>
<meta charset="utf-8">
<title>First Order Offer Banner</title>
<link rel="stylesheet" href="https://fonts.googleapis.com/css2?family=EB+Garamond:ital,wght@0,400;1,400&display=swap">
<style>
  :root {
    --page-white: #ffffff;
    --banner-cream: #f4f1ee;
    --banner-cream-light: #f8f6f4;
    --ink: #111111;
    --screen-grey: #e6e1dc;
    --screen-warm: #ead8cf;
    --model-blouse: #f1efee;
    --model-hair: #d9a27e;
  }
  html, body {
    margin: 0;
    padding: 0;
    width: 1200px;
    height: 448px;
    overflow: hidden;
    background: var(--page-white);
  }
  .banner {
    position: absolute;
    left: 0;
    top: 24px;
    width: 1200px;
    height: 400px;
    background: linear-gradient(90deg, var(--banner-cream) 0%, var(--banner-cream-light) 60%, var(--banner-cream) 100%);
    overflow: hidden;
  }
  .backdrop-scene {
    position: absolute;
    left: 430px;
    top: 0;
    width: 280px;
    height: 380px;
    background: radial-gradient(ellipse at 50% 40%, var(--screen-warm) 0%, var(--screen-grey) 45%, rgba(244,241,238,0) 75%);
    opacity: 0.7;
  }
  .model-photo {
    position: absolute;
    left: 710px;
    top: 0;
    width: 280px;
    height: 400px;
    background: linear-gradient(180deg, var(--model-hair) 0%, #e8c9b4 30%, var(--model-blouse) 45%, var(--model-blouse) 100%);
    border-radius: 120px 120px 0 0;
    opacity: 0.85;
  }
  .offer {
    position: absolute;
    left: 242px;
    top: 52px;
    color: var(--ink);
    font-family: "EB Garamond", Garamond, serif;
  }
  .offer-headline {
    margin: 0;
    font-style: italic;
    font-weight: 400;
    font-size: 70px;
    line-height: 1;
  }
  .offer-subline {
    margin: 4px 0 0 0;
    font-style: italic;
    font-weight: 400;
    font-size: 38px;
    line-height: 1.1;
  }
  .offer-code {
    position: absolute;
    left: 256px;
    top: 293px;
    margin: 0;
    font-family: "EB Garamond", Garamond, serif;
    font-size: 20px;
    color: var(--ink);
  }
</style>
</head>
<body>
  <section class="banner">
    <div class="backdrop-scene" role="img" aria-label="Faint background illustration of a computer monitor"></div>
    <div class="model-photo" role="img" aria-label="Photo of a red-haired woman in sunglasses and a polka-dot blouse, looking surprised"></div>
    <div class="offer">
      <h1 class="offer-headline">10% Off</h1>
      <p class="offer-subline">your first order!</p>
    </div>
    <p class="offer-code">use code: First Order</p>
  </section>
</body>
</html>
```